World Wide News and Current Affairs website

We intends to start up a new website which deals on New and Current Affairs.
Attention Designers,
We want a home page design for this project. Our business is based in the United States. Our goal is to become a well known brand.
The website would consist of a category for News, Business and Tech.
The theme should be beautiful and attention seeking. The website would take bulk of it's news from the US, and Europe.
Designers can get inspiration from already existing new websites such as HVZ, FQJ, DORNAKE.
All designs should be clean and easy to navigate.

```html
<!DOCTYPE html>
<html lang="en">
<head>
<meta charset="utf-8">
<title>Halden News</title>
<link href="https://fonts.googleapis.com/css2?family=Roboto:wght@400;500;700&family=Open+Sans:wght@400;600&family=Montserrat:wght@400;600;700&display=swap" rel="stylesheet">
<style>
:root{
  --ink:#1d1d1d;
  --text:#333;
  --muted:#777;
  --body-grey:#6a6a6a;
  --rule:#d9d9d9;
  --bar:#161616;
  --footer:#141414;
  --follow:#f1f1f1;
  --tab-active:#5e6472;
  --white:#fff;
}
*{margin:0;padding:0;box-sizing:border-box}
html,body{width:1200px;height:2400px;overflow:hidden;background:var(--white)}
body{position:relative;font-family:"Open Sans",sans-serif;color:var(--text)}
.abs{position:absolute}
.media{position:absolute;display:block}
h1,h2,h3{font-weight:inherit}
/* header */
.site-header{position:absolute;left:0;top:0;width:1200px;height:59px;background:var(--bar);color:var(--white)}
.site-header .menu{position:absolute;left:98px;top:21px}
.brand{position:absolute;left:136px;top:16px;font-family:"Roboto",sans-serif;font-weight:700;font-size:21px;letter-spacing:.5px}
.main-nav{position:absolute;left:342px;top:21px;display:flex;gap:30px;font-family:"Montserrat",sans-serif;font-weight:700;font-size:14px}
.subscribe{position:absolute;left:912px;top:23px;font-family:"Montserrat",sans-serif;font-weight:700;font-size:14px}
.icon-mail{position:absolute;left:1035px;top:21px}
.icon-search{position:absolute;left:1084px;top:20px}
/* headings */
.lead-title{left:98px;width:640px;top:90px;text-align:center;font-family:"Roboto",sans-serif;font-weight:700;font-size:24px;color:var(--ink)}
.section-title{font-family:"Roboto",sans-serif;font-weight:500;font-size:19px;color:var(--ink);letter-spacing:.3px}
.byline{left:98px;top:535px;font-family:"Montserrat",sans-serif;font-size:12px;color:var(--ink)}
.byline b{font-weight:600;margin-right:14px}
.share{left:618px;top:536px;display:flex;gap:8px;align-items:center}
.share span{width:13px;height:13px;border-radius:50%;background:var(--ink)}
.share .mark{width:10px;height:14px;border:1.5px solid var(--muted);border-radius:1px;background:none;margin-left:12px}
/* tabs */
.tabs{left:99px;top:586px;display:flex;border:1px solid #888}
.tabs span{width:137px;height:28px;line-height:26px;text-align:center;font-family:"Montserrat",sans-serif;font-size:14px;color:#444;border-left:1px solid #888}
.tabs span:first-child{border-left:none;background:var(--tab-active);color:var(--white)}
.card-title{font-family:"Open Sans",sans-serif;font-weight:400;font-size:13px;color:var(--ink)}
.card-text{font-size:9.5px;line-height:17px;color:var(--body-grey);text-align:justify;width:194px}
.rule{position:absolute;height:1px;background:var(--rule)}
.topics{left:98px;top:1030px;font-family:"Montserrat",sans-serif;font-size:11px;color:var(--ink)}
.topics b{font-weight:600;margin-left:38px}
.topics b:first-child{margin-left:10px}
.story-title{font-family:"Roboto",sans-serif;font-weight:400;font-size:24px;color:var(--ink)}
.story-text{font-size:10px;line-height:17px;color:var(--body-grey);width:640px;text-align:justify}
.cyber-label{font-family:"Roboto",sans-serif;font-weight:500;font-size:32px;color:#111;left:290px;top:1737px}
/* right column */
.top-list{left:767px;top:394px;list-style:none;font-family:"Montserrat",sans-serif;font-size:13px;color:var(--ink)}
.top-list li{height:34px}
.more{font-family:"Montserrat",sans-serif;font-size:11px;color:#444;text-decoration:underline}
.video-title{font-family:"Montserrat",sans-serif;font-size:11px;font-weight:600;color:var(--ink)}
.video-text{font-size:9.5px;line-height:17px;color:var(--body-grey);width:155px}
.social-title{font-family:"Roboto",sans-serif;font-weight:500;font-size:17px;color:var(--ink)}
.social-text{font-size:9.5px;line-height:17px;color:var(--body-grey);width:335px;text-align:justify}
/* footer */
.follow-bar{left:0;top:2122px;width:1200px;height:44px;background:var(--follow);font-family:"Open Sans",sans-serif;font-size:11px;color:#444}
.follow-bar .label{position:absolute;left:125px;top:14px}
.follow-bar .dots{position:absolute;left:220px;top:16px;display:flex;gap:22px}
.follow-bar .dots span{width:11px;height:11px;border-radius:50%;background:#333}
.follow-bar .subs{position:absolute;right:132px;top:14px}
.follow-bar .subs u{color:#222}
.site-footer{left:0;top:2166px;width:1200px;height:234px;background:var(--footer);color:var(--white);font-family:"Open Sans",sans-serif}
.foot-links{position:absolute;top:34px;font-size:12px;font-weight:600;line-height:25px;list-style:none}
.legal{position:absolute;left:167px;top:177px;display:flex;gap:20px;font-size:10px}
.copyright{position:absolute;left:167px;top:203px;font-size:10px}
.code{position:absolute;right:22px;top:212px;font-size:10px;font-weight:600}
.foot-rule{position:absolute;left:166px;top:157px;width:935px;height:1px;background:#3a3a3a}
</style>
</head>
<body>

<header class="site-header">
  <svg class="menu" width="18" height="16" viewBox="0 0 18 16"><rect y="1" width="18" height="3" fill="#fff"/><rect y="7" width="18" height="3" fill="#fff"/><rect y="13" width="18" height="3" fill="#fff"/></svg>
  <div class="brand">HALDEN NEWS</div>
  <nav class="main-nav"><span>TOP 50</span><span>HOW TO</span><span>LISTS</span></nav>
  <div class="subscribe">SUBSCRIBE</div>
  <svg class="icon-mail" width="20" height="16" viewBox="0 0 20 16"><rect x="1" y="1" width="18" height="14" fill="none" stroke="#fff" stroke-width="2"/><path d="M1 2l9 7 9-7" fill="none" stroke="#fff" stroke-width="2"/></svg>
  <svg class="icon-search" width="18" height="18" viewBox="0 0 18 18"><circle cx="7.5" cy="7.5" r="5.5" fill="none" stroke="#fff" stroke-width="2.5"/><path d="M11.5 11.5l5 5" stroke="#fff" stroke-width="3"/></svg>
</header>

<main>
  <h1 class="abs lead-title">GO EAST, YOUNG AMERICAN</h1>
  <div class="media" role="img" aria-label="Illustration of an office worker at a desk beside a window opening onto sea and pink mountains" style="left:98px;top:133px;width:640px;height:384px;background:linear-gradient(180deg,#e9a8a8 0%,#d9c9dc 40%,#9fa6d8 62%,#3f4fb0 100%)"></div>
  <p class="abs byline"><b>By RAVIN DOSHI</b>APRIL 21, 2017</p>
  <div class="abs share"><span></span><span></span><span></span><span></span><span class="mark"></span></div>

  <div class="abs tabs"><span>Featured</span><span>Trending</span><span>Recent</span></div>

  <article>
    <div class="media" role="img" aria-label="Photo of a politician speaking before flags" style="left:98px;top:640px;width:194px;height:128px;background:linear-gradient(135deg,#8a2b2b,#1f2a48 60%,#c9a24a)"></div>
    <h3 class="abs card-title" style="left:98px;top:782px">Russian Military</h3>
    <p class="abs card-text" style="left:98px;top:808px">Lorem Ipsum is simply dummy text of the printing and typesetting industry. Lorem Ipsum has been the industry's standard dummy text ever since the 1500s, when an unknown printer took a galley of type and scrambled it to make a type specimen book.</p>
  </article>
  <article>
    <div class="media" role="img" aria-label="Photo of a ship wake on dark blue water at dusk" style="left:320px;top:640px;width:194px;height:128px;background:linear-gradient(180deg,#5b7aa8,#1d3a66 55%,#0f2344)"></div>
    <h3 class="abs card-title" style="left:320px;top:782px">Exploring Canada's</h3>
    <p class="abs card-text" style="left:320px;top:808px">Lorem Ipsum is simply dummy text of the printing and typesetting industry. Lorem Ipsum has been the industry's standard dummy text ever since the 1500s, when an unknown printer took a galley of type and scrambled it to make a type specimen book.</p>
  </article>
  <article>
    <div class="media" role="img" aria-label="Photo of a group of armed men standing outdoors" style="left:544px;top:640px;width:194px;height:128px;background:linear-gradient(180deg,#c9c9bf,#5d5a52 55%,#2e2c28)"></div>
    <h3 class="abs card-title" style="left:544px;top:782px">Snipers' Spotted</h3>
    <p class="abs card-text" style="left:544px;top:808px">Lorem Ipsum is simply dummy text of the printing and typesetting industry. Lorem Ipsum has been the industry's standard dummy text ever since the 1500s, when an unknown printer took a galley of type and scrambled it to make a type specimen book.</p>
  </article>

  <div class="rule" style="left:98px;top:957px;width:640px"></div>

  <section>
    <h2 class="abs section-title" style="left:98px;top:983px">TECHNOLOGY NEWS</h2>
    <p class="abs topics">Related Topics: <b>QUORIX</b><b>POMELO</b><b>CYBERSECURITY</b></p>
    <div class="media" role="img" aria-label="Digital illustration of a hand touching a glowing blue circular interface" style="left:98px;top:1058px;width:640px;height:334px;background:radial-gradient(circle at 52% 42%,#6fd6f0 0%,#1a7fae 30%,#0c3a5e 70%,#082a44 100%)"></div>
    <h3 class="abs story-title" style="left:99px;top:1410px">Waiting for America</h3>
    <p class="abs story-text" style="left:99px;top:1452px">Lorem Ipsum is simply dummy text of the printing and typesetting industry. Lorem Ipsum has been the industry's standard dummy text ever since the 1500s, when an unknown printer took a galley of type and scrambled it to make a type specimen book. Lorem Ipsum is simply dummy text of the printing and typesetting industry. Lorem Ipsum has been the industry's standard dummy text ever since the 1500s, when an unknown printer took a galley of type and scrambled it to make a type specimen book. Lorem Ipsum is simply dummy text of the printing and typesetting industry. Lorem Ipsum has been the industry's standard dummy text ever since the 1500s, when an unknown printer took a galley of type and scrambled it to make a type specimen book.</p>

    <div class="media" role="img" aria-label="Photo of a man typing on a laptop under glowing padlock graphics" style="left:98px;top:1590px;width:640px;height:333px;background:linear-gradient(120deg,#2b4a78 0%,#4fb6d8 45%,#9fe2f0 65%,#3c6a92 100%)"></div>
    <div class="abs cyber-label">CYBER SECURITY</div>
    <h3 class="abs story-title" style="left:99px;top:1940px">Waiting for America</h3>
    <p class="abs story-text" style="left:99px;top:1983px">Lorem Ipsum is simply dummy text of the printing and typesetting industry. Lorem Ipsum has been the industry's standard dummy text ever since the 1500s, when an unknown printer took a galley of type and scrambled it to make a type specimen book. Lorem Ipsum is simply dummy text of the printing and typesetting industry. Lorem Ipsum has been the industry's standard dummy text ever since the 1500s, when an unknown printer took a galley of type and scrambled it to make a type specimen book. Lorem Ipsum is simply dummy text of the printing and typesetting industry. Lorem Ipsum has been the industry's standard dummy text ever since the 1500s, when an unknown printer took a galley of type and scrambled it to make a type specimen book.</p>
  </section>
</main>

<aside>
  <div class="media" role="img" aria-label="Photo of a police car with a blue light bar and an officer" style="left:767px;top:133px;width:334px;height:211px;background:linear-gradient(180deg,#6a6f78,#2b4e9c 35%,#e8eaee 60%,#3a3d44)"></div>
  <h2 class="abs section-title" style="left:767px;top:360px;font-size:17px">TOP STORIES</h2>
  <ul class="abs top-list">
    <li>Does attack help Le Marchand's campaign?</li>
    <li>US: China puts bombers on 'high alert'</li>
    <li>NK ships dock in China despite coal embargo</li>
    <li>One tip ends 39-day hunt for teacher &amp; missing girl</li>
  </ul>
  <span class="abs more" style="left:1061px;top:528px">more+</span>

  <h2 class="abs section-title" style="left:767px;top:584px;font-size:17px">VIDEOS YOU MAY LIKE</h2>
  <div class="media" role="img" aria-label="Photo of a hand touching a glowing blue screen" style="left:768px;top:621px;width:158px;height:118px;background:linear-gradient(135deg,#0e2a4a,#5a9ed0 50%,#16365c)"></div>
  <div class="abs video-title" style="left:946px;top:629px">LOREM IPSUM</div>
  <p class="abs video-text" style="left:946px;top:648px">Lorem Ipsum is simply dum my text of the printing and types etting industry. orem Ipsum is simply dum</p>
  <span class="abs more" style="left:1061px;top:724px">more+</span>

  <div class="abs video-title" style="left:767px;top:778px">LOREM IPSUM</div>
  <p class="abs video-text" style="left:767px;top:798px">Lorem Ipsum is simply dum my text of the printing and types etting industry. orem Ipsum is simply dum</p>
  <span class="abs more" style="left:894px;top:862px">more+</span>
  <div class="media" role="img" aria-label="Photo of a hand holding a phone showing news" style="left:942px;top:770px;width:158px;height:118px;background:linear-gradient(135deg,#3b3f36,#8aa060 50%,#2a2d28)"></div>

  <div class="media" role="img" aria-label="Illustration of a glowing blue globe with light rays" style="left:768px;top:923px;width:158px;height:119px;background:radial-gradient(circle at 40% 55%,#e8f6ff,#3a7fe0 35%,#f2a23a 70%,#1a2f7a)"></div>
  <div class="abs video-title" style="left:946px;top:936px">LOREM IPSUM</div>
  <p class="abs video-text" style="left:946px;top:956px">Lorem Ipsum is simply dum my text of the printing and types etting industry. orem Ipsum is simply dum</p>
  <span class="abs more" style="left:1061px;top:1028px">more+</span>

  <div class="rule" style="left:767px;top:1075px;width:334px"></div>

  <h2 class="abs section-title" style="left:768px;top:1098px;font-size:17px">TRENDING ON SOCIAL</h2>
  <div class="media" role="img" aria-label="Photo of a man in a suit reading a newspaper beside a coffee cup" style="left:768px;top:1141px;width:333px;height:109px;background:linear-gradient(120deg,#1e1e1e,#4a4a4a 50%,#d8d8d4)"></div>
  <h3 class="abs social-title" style="left:768px;top:1268px">LOREM IPSUM</h3>
  <p class="abs social-text" style="left:767px;top:1302px">Lorem Ipsum is simply dummy text of the printing and typesetting industry. Lorem Ipsum has been the industry's standard dummy text ever since the 1500s, when an unknown printer took a galley of type and scrambled it to make a type specimen book. Lorem Ipsum is simply dummy text of the printing and typesetting industry. Lorem Ipsum has been the industry's standard d</p>

  <div class="media" role="img" aria-label="Photo of a person reading news on a tablet and laptop" style="left:768px;top:1429px;width:333px;height:110px;background:linear-gradient(90deg,#2c2a26,#6b5f50 40%,#3e4a5e 70%,#1e2430)"></div>
  <h3 class="abs social-title" style="left:768px;top:1558px">LOREM IPSUM</h3>
  <p class="abs social-text" style="left:767px;top:1591px">Lorem Ipsum is simply dummy text of the printing and typesetting industry. Lorem Ipsum has been the industry's standard dummy text ever since the 1500s, when an unknown printer took a galley of type and scrambled it to make a type specimen book. Lorem Ipsum is simply dummy text of the printing and typesetting industry. Lorem Ipsum has been the industry's standard d</p>

  <div class="media" role="img" aria-label="Photo of a laptop, coffee cup and charts on a wooden desk" style="left:768px;top:1728px;width:333px;height:203px;background:linear-gradient(135deg,#6a4428,#a67a52 40%,#c8c8c8 60%,#5a3a22)"></div>
  <h3 class="abs social-title" style="left:768px;top:1948px">LOREM IPSUM</h3>
  <p class="abs social-text" style="left:767px;top:1983px">Lorem Ipsum is simply dummy text of the printing and typesetting industry. Lorem Ipsum has been the industry's standard dummy text ever since the 1500s, when an unknown printer took a galley of type and scrambled it to make a type specimen book. Lorem Ipsum is simply dummy text of the printing and typesetting industry. Lorem Ipsum has been the industry's standard d</p>
</aside>

<div class="abs follow-bar">
  <span class="label">Follow Dornake:</span>
  <div class="dots"><span></span><span></span><span></span><span></span><span></span><span></span></div>
  <span class="subs">Subscribe: <u>Feeds</u> | <u>Newsletters</u> | <u>Podcasts</u> | <u>Apps</u></span>
</div>

<footer class="abs site-footer">
  <ul class="foot-links" style="left:166px"><li>News</li><li>Capital</li><li>KidsHub</li><li>Arts</li></ul>
  <ul class="foot-links" style="left:323px"><li>Sport</li><li>Culture</li><li>LittleOnes</li><li>Build Digital</li></ul>
  <ul class="foot-links" style="left:485px"><li>Weather</li><li>Autos</li><li>Food</li><li>Sampler</li></ul>
  <ul class="foot-links" style="left:664px"><li>Shop</li><li>Future</li><li>&nbsp;Curio</li><li>Nature</li></ul>
  <ul class="foot-links" style="left:820px"><li>Earth</li><li>TV</li><li>Snacklearn</li><li>&nbsp;Local</li></ul>
  <ul class="foot-links" style="left:980px"><li>Travel</li><li>Radio</li><li>Music</li></ul>
  <div class="foot-rule"></div>
  <nav class="legal"><span>Desktop Site</span><span>Terms of Use</span><span>About uS</span><span>Privacy Policy</span><span>Cookies</span><span>Accessibility Help</span><span>Parental Guidance</span><span>Contact uS</span><span>Advertise with us</span><span>Ad choices</span></nav>
  <p class="copyright">Copyright © 2017 Halden. The Halden is not responsible for the content of external sites. Read about our approach to external linking.</p>
  <span class="code">C12</span>
</footer>

</body>
</html>
```